New Dental Office Needs an Attractive and user friendly Website Designed

I need a website for a new dental office. The Name is Maplecrest Dentistry. I would like a Modern design with a user friendly interface and usability.
I would like a landing page, a page that lists the services we offer: Cosmetic Dentistry, Implants, Dental Hygiene, Emergency Services, Restorations, Dentures
Target Market(s)
Mid to upper class
Industry/Entity Type
Dentistry
Coding
Coded - Design and coding required
Number of Pages Required
1 page
Requirements
Must have
- Landing page that has a scheduling option, Procedures, operating hours, and contact us info
Nice to have
- Appealing design, Soft comforting colors. Easy to navigate page, Modern and professional.

```html
<!DOCTYPE html>
<html lang="en">
<head>
<meta charset="utf-8">
<title>Maplecrest Dentistry</title>
<link href="https://fonts.googleapis.com/css2?family=Poppins:wght@300;400;500;600;700&display=swap" rel="stylesheet">
<style>
:root{
  --ink:#0f2a22;
  --deep:#0f2e25;
  --forest:#2a6453;
  --sage:#b3d4c3;
  --mint-a:#a0f5dc;
  --mint-b:#e8fdf6;
  --text-green:#1e5a47;
  --muted:#8fa59b;
  --white:#ffffff;
}
*{box-sizing:border-box;margin:0;padding:0}
html,body{width:1200px;height:1200px;overflow:hidden;background:var(--white);font-family:'Poppins',sans-serif}
.stage{position:absolute;left:0;top:0;width:1920px;height:1920px;transform:scale(.625);transform-origin:0 0}
.page{position:absolute;left:610px;top:10px;width:676px;height:1895px;background:var(--white);color:var(--ink)}
.abs{position:absolute}
/* header */
.topbar{left:0;top:0;width:676px;height:40px;background:var(--ink)}
.brand-box{left:0;top:0;width:130px;height:40px;background:#111;border-right:4px solid var(--white);display:flex;align-items:center;justify-content:center}
.brand-name{font-size:11px;font-weight:500;color:var(--white);text-align:center;line-height:1.1}
.nav{left:182px;top:14px;display:flex;gap:11px;font-size:5.5px;font-weight:600;color:var(--white);align-items:center}
.nav .cta{background:var(--white);color:var(--ink);padding:3px 5px;border-radius:1px;font-weight:500}
.acct{top:13px;height:15px;border:1px solid var(--white);border-radius:8px;color:var(--white);font-size:5px;font-weight:600;display:flex;align-items:center;justify-content:center;gap:3px}
.subbar{left:0;top:40px;width:676px;height:15px;background:var(--sage);font-size:5px;color:var(--white);font-weight:600}
/* hero */
.hero{left:0;top:55px;width:676px;height:282px;background:linear-gradient(120deg,#7fb59d 0%,#b7d6c6 40%,#dfeee6 70%,#a9c8b9 100%)}
.hero-veil{left:101px;top:51px;width:473px;height:166px;background:rgba(255,255,255,.45);text-align:center;color:var(--forest)}
.hero-welcome{font-size:32px;font-weight:300;margin-top:16px;color:#8fbfae}
.hero-name{font-size:40px;font-weight:500;color:var(--forest);opacity:.75;line-height:1.1;margin-top:4px}
/* about */
.h2{font-weight:500;color:var(--deep)}
.about-title{left:58px;top:405px;font-size:16px}
.about-copy{left:58px;top:436px;width:262px;font-size:6.8px;line-height:1.7;color:var(--text-green);font-weight:300}
.about-photo{left:342px;top:405px;width:261px;height:145px;background:linear-gradient(90deg,#2f4766,#41608b 50%,#23344f)}
/* treatments */
.treat{left:0;top:620px;width:676px;height:193px;background:linear-gradient(90deg,var(--mint-a),var(--mint-b))}
.treat-title{left:0;width:676px;top:39px;text-align:center;font-size:16px}
.treat-label{left:213px;top:69px;font-size:6.5px}
.treat-select{left:213px;top:83px;width:248px;height:22px;background:var(--white);font-size:6px;padding:0 8px;display:flex;align-items:center;justify-content:space-between}
/* services */
.svc-title{left:0;width:676px;top:855px;text-align:center;font-size:16px}
.svc-sub{left:0;width:676px;top:884px;text-align:center;font-size:6.5px}
.svc-band{left:0;top:875px;width:676px;height:472px}
.card{width:175px;height:189px;background:var(--white);box-shadow:0 1px 4px rgba(0,0,0,.2);padding:5px}
.card-photo{width:165px;height:106px}
.card-title{text-align:center;font-size:8px;font-weight:700;margin-top:9px}
.card-text{text-align:center;font-size:5.8px;color:var(--muted);line-height:1.6;margin-top:2px;font-weight:300}
.card-btn{margin-top:6px;height:19px;background:var(--deep);color:var(--white);font-size:6px;display:flex;align-items:center;justify-content:center}
/* contact */
.logo-box{left:127px;top:1421px;width:106px;height:38px;background:#111;display:flex;align-items:center;justify-content:center}
.info{left:60px;width:240px;top:1483px;text-align:center;font-size:7px;line-height:1.65;color:#333;font-weight:300}
.info b{font-weight:700;color:var(--ink)}
.contact-title{left:378px;width:200px;top:1378px;text-align:center;font-size:16px}
.lbl{left:352px;font-size:7px;color:#333}
.field{left:418px;width:200px;font-size:5.5px;color:#888;border-bottom:1px solid #eee}
.submit{left:415px;top:1609px;width:96px;height:20px;background:var(--deep);color:var(--white);font-size:6.5px;letter-spacing:1.5px;display:flex;align-items:center;justify-content:center}
/* footer */
.footer{left:0;top:1620px;width:676px;height:275px}
.ft-brand{left:52px;top:1790px;width:140px;text-align:center;color:var(--white);font-size:15px;font-weight:500;line-height:1.1}
.ft-col{top:1770px;color:#cfe3da;font-size:6px;line-height:1.7;font-weight:300}
.ft-col h4{font-size:9px;font-weight:400;color:var(--white);line-height:1.4}
.ft-col b{font-weight:600;color:var(--white)}
.social{display:flex;gap:16px;margin-top:6px}
.social span{width:13px;height:13px;border-radius:50%;background:var(--white);display:block}
</style>
</head>
<body>
<div class="stage">
<div class="page">

  <header>
    <div class="abs topbar"></div>
    <div class="abs brand-box"><div class="brand-name">Maplecrest<br>Dentistry</div></div>
    <nav class="abs nav">
      <span>About</span><span>Treatments and Procedures</span><span>Services</span><span>Contact Us</span><span>FAQs</span><span class="cta">Request Appoinment</span>
    </nav>
    <div class="abs acct" style="left:560px;width:36px">&#10140; Join</div>
    <div class="abs acct" style="left:605px;width:46px">&#9679; Sign-in</div>
    <div class="abs subbar">
      <span class="abs" style="left:502px;top:4px">&#9990; +123 4444 5555</span>
      <span class="abs" style="left:579px;top:4px">&#9993; abc@example.com</span>
    </div>
  </header>

  <section class="abs hero" role="img" aria-label="Bright modern dental treatment room with chairs and overhead lamp">
    <div class="abs hero-veil">
      <div class="hero-welcome">Welcome</div>
      <div class="hero-name">Maplecrest Dentistry</div>
    </div>
    <svg class="abs" style="left:0;top:0" width="676" height="282" viewBox="0 0 676 282">
      <path d="M0 282 Q360 270 676 186 L676 282 Z" fill="#fff"/>
    </svg>
  </section>

  <section>
    <h2 class="abs h2 about-title">About Us</h2>
    <div class="abs about-copy">
      <p>We are a team of dedicated and clinically trained professionals. Our goal is to provide the best dental care with modern equipment.</p>
      <p style="margin-top:12px">Lorem ipsum dolor sit, amet consectetur adipisicing elit. Illo ex voluptatem aspernatur unde laudantium laborum esse in aut officia. Molestiae quibusdam facilis deleniti eum cum dolorum, repudiandae mollitia itaque eveniet.</p>
    </div>
    <div class="abs about-photo" role="img" aria-label="Smiling dental team in scrubs"></div>
  </section>

  <section class="abs treat">
    <h2 class="abs h2 treat-title">Treatments and Procedures</h2>
    <div class="abs treat-label">Search Treatments and Procedures topics:</div>
    <div class="abs treat-select"><span>Routine Treatment</span><span>&#8964;</span></div>
  </section>

  <section>
    <svg class="abs svc-band" width="676" height="472" viewBox="0 0 676 472">
      <path d="M0 80 Q340 70 676 0 L676 472 L0 472 Z" fill="#b3d4c3"/>
      <path d="M0 80 Q340 70 676 0 L676 16 Q340 84 0 92 Z" fill="#2a6453"/>
    </svg>
    <h2 class="abs h2 svc-title">Our Services</h2>
    <div class="abs svc-sub">Explore our range of dental care services.</div>

    <div class="abs card" style="left:53px;top:920px"><div class="card-photo" role="img" aria-label="Patient receiving cosmetic dental check" style="background:linear-gradient(120deg,#dfe6ea,#9fb0bc)"></div><div class="card-title">Cosmetic Dentistry</div><div class="card-text">Lorem ipsum dolor sit amet consectetur adipisicing elit. Consequatur, aperiam?</div><div class="card-btn">Read more</div></div>
    <div class="abs card" style="left:250px;top:920px"><div class="card-photo" role="img" aria-label="Patient reviewing implant scan on screen" style="background:linear-gradient(120deg,#cfd5d6,#6fa7a0)"></div><div class="card-title">Implants</div><div class="card-text">Lorem ipsum dolor sit amet consectetur adipisicing elit. Consequatur, aperiam?</div><div class="card-btn">Read more</div></div>
    <div class="abs card" style="left:447px;top:920px"><div class="card-photo" role="img" aria-label="Hygienist cleaning a patient's teeth" style="background:linear-gradient(120deg,#8a3a46,#b9c3cc)"></div><div class="card-title">Dental Hygiene</div><div class="card-text">Lorem ipsum dolor sit amet consectetur adipisicing elit. Consequatur, aperiam?</div><div class="card-btn">Read more</div></div>

    <div class="abs card" style="left:53px;top:1128px"><div class="card-photo" role="img" aria-label="Dentist explaining a tooth model to a patient" style="background:linear-gradient(120deg,#3a2f2c,#a3b1bd)"></div><div class="card-title">Emergency Services</div><div class="card-text">Lorem ipsum dolor sit amet consectetur adipisicing elit. Consequatur, aperiam?</div><div class="card-btn">Read more</div></div>
    <div class="abs card" style="left:250px;top:1128px"><div class="card-photo" role="img" aria-label="Dentist restoring a patient's tooth" style="background:linear-gradient(120deg,#c9d4da,#6b5047)"></div><div class="card-title">Restorations</div><div class="card-text">Lorem ipsum dolor sit amet consectetur adipisicing elit. Consequatur, aperiam?</div><div class="card-btn">Read more</div></div>
    <div class="abs card" style="left:447px;top:1128px"><div class="card-photo" role="img" aria-label="Hand holding a set of dentures" style="background:linear-gradient(120deg,#e6b7a4,#cfe1ea)"></div><div class="card-title">Dentures</div><div class="card-text">Lorem ipsum dolor sit amet consectetur adipisicing elit. Consequatur, aperiam?</div><div class="card-btn">Read more</div></div>
  </section>

  <section>
    <div class="abs logo-box"><div class="brand-name">Maplecrest<br>Dentistry</div></div>
    <div class="abs info">
      <b>Hours Operation</b><br>
      Monday - Friday : 10.30 am - 8.30 pm<br>
      Saturday : 10.30 am - 7.00 pm<br>
      Sunday/Public Holidays: Closed<br><br>
      &#9990; +123 444 555<br>
      &#9993; abc@example.com<br>
      Harbour Lane, Fairhaven NSW 2099, <b style="font-weight:500">Australia</b><br>
      PO BOX 118: Glenmore SA 5250, <b style="font-weight:500">Australia</b>
    </div>

    <h2 class="abs h2 contact-title">Contact Us</h2>
    <div class="abs lbl" style="top:1409px">First Name</div>
    <div class="abs field" style="top:1405px;height:20px;padding:6px 3px">Your name..</div>
    <div class="abs lbl" style="top:1442px">Last Name</div>
    <div class="abs field" style="top:1438px;height:20px;padding:6px 3px">Your last name..</div>
    <div class="abs lbl" style="top:1477px">Country</div>
    <div class="abs field" style="top:1472px;height:20px;padding:6px 4px;color:#333;display:flex;justify-content:space-between"><span>Australia</span><span>&#8964;</span></div>
    <div class="abs lbl" style="top:1554px">Subject</div>
    <div class="abs field" style="top:1505px;height:95px;padding:6px 3px;border:1px solid #f0f0f0">Write something..</div>
    <div class="abs submit">Submit</div>
  </section>

  <footer>
    <svg class="abs footer" width="676" height="275" viewBox="0 0 676 275">
      <path d="M0 115 Q360 100 676 0 L676 20 Q360 115 0 126 Z" fill="#b3d4c3"/>
      <path d="M0 126 Q360 115 676 20 L676 275 L0 275 Z" fill="#2a6453"/>
    </svg>
    <div class="abs ft-brand">Maplecrest<br>Dentistry</div>
    <div class="abs ft-col" style="left:202px">
      <h4>Address</h4>
      &#9990; +123 444 555<br>&#9993; abc@example.com<br>Harbour Lane, Fairhaven NSW 2099,<br><b>Australia</b><br>PO BOX 118: Glenmore SA 5250,<br><b>Australia</b>
    </div>
    <div class="abs ft-col" style="left:375px">
      <h4>Menu</h4>
      About Us<br>Treatments and Procedures<br>Services<br>Contact Us<br>FAQS<br>Request Appoinment
    </div>
    <div class="abs ft-col" style="left:490px">
      <h4>Social Media</h4>
      <div class="social"><span></span><span></span><span></span><span></span></div>
    </div>
  </footer>

</div>
</div>
</body>
</html>
```